Cosmetic Clinic Looking For Sign Designs

We are looking for sign design ideas for the front of our building and a lawn sign for our cosmetic injection salon.
I have uploaded the front of our building for a mock up and size, lawn posts with size and a sign that uses the same dimensions.
We would like both signs to be black for the background.

Target Market(s)

Ages 18-75

Industry/Entity Type

Beauty

Requirements
Must have
• Services we offer:
• Cosmetic Injections
• Airbrush Spray Tanning
• Eyelash Growth Serum
• Skin Care Products & More
• Everything must be on a black background
• The lawn sign must have the address: 394 Fenwick and the building sign should have the phone number.
Should not have
• Nothing can light up (no LED)
• Both signs do not need the full address. Just 394 Fenwick and the phone number

```html
<!DOCTYPE html>
<html lang="en">
<head>
<meta charset="utf-8">
<title>Bright Bloom Salon – Building Sign</title>
<link href="https://fonts.googleapis.com/css2?family=Roboto:wght@900&family=Open+Sans:wght@400&family=Oswald:wght@400;600&display=swap" rel="stylesheet">
<style>
  :root {
    --sign-black: #000000;
    --page-bg: #e6e6e6;
    --cyan: #2bb6d6;
    --pink: #ec1a7e;
    --lavender: #7478c0;
    --white: #ffffff;
    --window-light: #d9d8d2;
    --window-dark: #4a4d50;
  }
  html, body {
    margin: 0;
    padding: 0;
    width: 900px;
    height: 1200px;
    overflow: hidden;
    background: var(--page-bg);
  }
  .canvas {
    position: relative;
    width: 900px;
    height: 1200px;
  }
  .sign {
    position: absolute;
    left: 20px;
    top: 307px;
    width: 860px;
    height: 585px;
    background: var(--sign-black);
    overflow: hidden;
  }
  .sign__swoosh {
    position: absolute;
    inset: 0;
  }
  .brand-mark {
    position: absolute;
    left: 76px;
    top: 27px;
    width: 124px;
    height: 124px;
    border-radius: 50%;
    background: var(--lavender);
  }
  .brand-name {
    position: absolute;
    left: 232px;
    top: 38px;
    margin: 0;
    font-family: "Roboto", sans-serif;
    font-weight: 900;
    font-size: 58px;
    line-height: 1;
    letter-spacing: 1px;
    color: var(--cyan);
    white-space: nowrap;
  }
  .brand-descriptor {
    position: absolute;
    left: 234px;
    top: 108px;
    width: 398px;
    display: flex;
    align-items: center;
    gap: 14px;
    font-family: "Open Sans", sans-serif;
    font-size: 38px;
    line-height: 1;
    letter-spacing: 2px;
    color: var(--pink);
  }
  .brand-descriptor::before,
  .brand-descriptor::after {
    content: "";
    flex: 1;
    height: 3px;
    background: var(--pink);
  }
  .window {
    position: absolute;
    top: 171px;
    height: 319px;
    background: var(--sign-black);
    box-shadow: inset 0 0 0 1px #1a1a1a;
  }
  .window--left { left: 82px; width: 246px; }
  .window--right { left: 526px; width: 254px; }
  .window__view {
    position: absolute;
    inset: 16px 16px 18px 16px;
    background: linear-gradient(180deg, var(--window-light) 0%, var(--window-dark) 12%, var(--window-dark) 88%, var(--window-light) 100%);
  }
  .services {
    position: absolute;
    left: 320px;
    top: 188px;
    width: 220px;
    margin: 0;
    padding: 0;
    list-style: none;
    text-align: center;
    font-family: "Oswald", sans-serif;
    font-weight: 600;
    font-size: 24px;
    line-height: 26px;
    text-transform: uppercase;
    color: var(--white);
    white-space: nowrap;
  }
  .services__item {
    margin: 0 0 19px;
    transform: scaleX(0.9);
  }
  .services__item:last-child { margin-bottom: 0; }
  .services__rule {
    position: absolute;
    top: 477px;
    height: 3px;
    width: 74px;
    background: var(--pink);
  }
  .services__rule--left { left: 344px; }
  .services__rule--right { left: 445px; }
  .contact {
    position: absolute;
    left: 82px;
    top: 512px;
    display: flex;
    align-items: center;
    gap: 10px;
    font-family: "Oswald", sans-serif;
    font-weight: 400;
    font-size: 31px;
    line-height: 1;
    white-space: nowrap;
  }
  .contact__bullet {
    width: 11px;
    height: 11px;
    border-radius: 50%;
    background: var(--white);
  }
  .contact__phone { color: var(--lavender); margin-right: 6px; }
  .contact__web { color: var(--pink); }
</style>
</head>
<body>
<div class="canvas">
  <section class="sign" aria-label="Bright Bloom Salon building sign">
    <svg class="sign__swoosh" width="860" height="585" viewBox="0 0 860 585" aria-hidden="true">
      <circle cx="1010" cy="370" r="408" fill="none" stroke="var(--pink)" stroke-width="14"/>
      <circle cx="1010" cy="370" r="372" fill="var(--lavender)"/>
      <circle cx="1010" cy="370" r="336" fill="none" stroke="var(--sign-black)" stroke-width="8"/>
    </svg>

    <div class="brand-mark" aria-hidden="true"></div>
    <h1 class="brand-name">BRIGHT BLOOM</h1>
    <div class="brand-descriptor">SALON</div>

    <div class="window window--left">
      <div class="window__view" role="img" aria-label="Building window showing through the sign"></div>
    </div>

    <ul class="services">
      <li class="services__item">Cosmetic<br>Injections</li>
      <li class="services__item">Airbrush<br>Spray Tanning</li>
      <li class="services__item">Eyelash<br>Growth Serum</li>
      <li class="services__item">Skin Care<br>Products &amp; More</li>
    </ul>
    <span class="services__rule services__rule--left"></span>
    <span class="services__rule services__rule--right"></span>

    <div class="window window--right">
      <div class="window__view" role="img" aria-label="Building window showing through the sign"></div>
    </div>

    <div class="contact">
      <span class="contact__bullet"></span>
      <span class="contact__phone">(905) 555-0148</span>
      <span class="contact__bullet"></span>
      <span class="contact__web">BRIGHTBLOOMSALON.COM</span>
    </div>
  </section>
</div>
</body>
</html>
```